Visitenkarten-Design für ein Biotechnologieunternehmen
Zielgruppe
Wir sind ein Biotechnologieunternehmen, welches Enzyme für Kunden der Bereiche Chemie, Tierfutter, Pharma und Biotech mit Hilfe von high perfomance computing entwickeln.
Aufgabenstellung
Das Design sollte zu einem High-Tech-Unternehmen passen, modern und konservativ zu gleich, sowie professionell. Im Anhang findet sich ein PDF, in welchem unser Logo dargestellt ist. Jene Version des Fonts ' DINPro'(Seite 14) ist zu verwenden. Die anderen Entwürfe wurden verworfen.
Unsere Unternehmensfarbe ist in RGB: 0 - 90 -180
Das Logo sollte in dieser Farbe abgebildet werden. Der Untertitel unseres Unternehmens sollte ebenfalls auf der Visitenkarte verankert sein: 'next-generation enzyme design'
Zur Information, unsere Website ist 'www.vorelta.de'.
Informationen auf der Visitenkarte:
- Name des Unternehmens
- Name der Ansprechperson
- Jobtitel der Ansprechperson
- Adresse des Unternehmens
- E-Mail der Ansprechperson
- Telefonnummer der Ansprechperson
- Handynummer der Ansprechperson
- Webadresse des Unternehmens
Stockfotos dürfen verwendet werden und werden von uns im bei Auswahl des entsprechenden Entwurfes käuflich erworben. Kreative Freiheit bei der Gestaltung der Rückseite.
Als ausgeliefertes Format bitten wir um Microsoft Word, damit die konkreten Daten der Mitarbeiter im Nachgang von uns eingetragen werden können. Zur Bearbeitung von PDFs oder AI-Dateien mit Adobe Illustrator sind wir nicht in der Lage.

```html
<!DOCTYPE html>
<html lang="de">
<head>
<meta charset="utf-8">
<title>Vorelta – Visitenkarte</title>
<link rel="stylesheet" href="https://fonts.googleapis.com/css2?family=Open+Sans:wght@400;600;700&display=swap">
<style>
  :root {
    --brand: #005ab4;
    --brand-dark: #004a96;
    --paper: #ffffff;
    --ink: #1c1c1c;
    --grey-band: #c9cacc;
    --stage: #e7e9ec;
  }
  * { box-sizing: border-box; margin: 0; padding: 0; }
  html, body { width: 1200px; height: 912px; overflow: hidden; }
  body {
    background: var(--stage);
    font-family: "Open Sans", Arial, sans-serif;
    display: flex; flex-direction: column; align-items: center; justify-content: center;
    gap: 40px;
  }
  .card {
    position: relative;
    width: 620px; height: 401px;
    overflow: hidden;
    box-shadow: 0 8px 24px rgba(0,0,0,.18);
  }

  /* Front */
  .card--front { background: var(--brand); color: var(--paper); }
  .front-mark {
    position: absolute; left: 0; right: 0; top: 120px;
    display: flex; align-items: center; justify-content: center; gap: 16px;
  }
  .front-mark .dot {
    width: 26px; height: 26px; border: 5px solid var(--paper); border-radius: 50%;
  }
  .front-mark .name { font-size: 64px; font-weight: 600; letter-spacing: -.5px; line-height: 1; }
  .tagline {
    position: absolute; left: 0; right: 0; bottom: 78px;
    text-align: center; font-size: 19px; letter-spacing: 1px; text-transform: uppercase;
  }

  /* Back */
  .card--back { background: var(--paper); color: var(--ink); }
  .back-mark {
    position: absolute; right: 40px; top: 58px;
    display: flex; align-items: center; gap: 12px; color: var(--brand);
  }
  .back-mark .dot { width: 22px; height: 22px; border: 4px solid var(--brand); border-radius: 50%; }
  .back-mark .name { font-size: 58px; font-weight: 600; line-height: 1; letter-spacing: -.5px; }
  .address {
    position: absolute; right: 40px; top: 172px;
    text-align: right; font-size: 15px; line-height: 1.35;
  }
  .person { position: absolute; left: 40px; top: 212px; }
  .person .fullname { font-size: 24px; font-weight: 700; color: var(--brand); line-height: 1.1; }
  .person .role { font-size: 16px; margin-top: 2px; }
  .contacts { position: absolute; left: 40px; top: 282px; list-style: none; font-size: 16px; }
  .contacts li { display: flex; align-items: center; gap: 12px; height: 24px; }
  .contacts svg { width: 18px; height: 18px; flex: none; }
  .bands { position: absolute; left: 0; bottom: 0; width: 620px; height: 401px; }
  .website {
    position: absolute; right: 22px; bottom: 14px;
    color: var(--paper); font-size: 15px; letter-spacing: .2px;
  }
</style>
</head>
<body>

  <section class="card card--front" aria-label="Vorderseite">
    <div class="front-mark">
      <span class="dot"></span>
      <span class="name">vorelta</span>
    </div>
    <p class="tagline">Next-Generation Enzyme Design</p>
  </section>

  <section class="card card--back" aria-label="Rückseite">
    <svg class="bands" viewBox="0 0 620 401" aria-hidden="true">
      <path fill="var(--grey-band)" d="M0 390 L0 370 L405 370 C432 370 438 322 470 322 L620 322 L620 345 L492 345 C462 345 456 390 430 390 Z"/>
      <path fill="var(--brand)" d="M0 401 L0 390 L430 390 C456 390 462 345 492 345 L620 345 L620 401 Z"/>
    </svg>

    <div class="back-mark">
      <span class="dot"></span>
      <span class="name">vorelta</span>
    </div>

    <p class="address">Kelterstraße 18<br>D - 70199 Stuttgart</p>

    <div class="person">
      <p class="fullname">Jonas Albrecht</p>
      <p class="role">Managing Director</p>
    </div>

    <ul class="contacts">
      <li>
        <svg viewBox="0 0 24 24"><path fill="var(--brand)" d="M6.6 10.8a15.1 15.1 0 0 0 6.6 6.6l2.2-2.2a1 1 0 0 1 1-.25 11.4 11.4 0 0 0 3.6.57 1 1 0 0 1 1 1V20a1 1 0 0 1-1 1A17 17 0 0 1 3 4a1 1 0 0 1 1-1h3.5a1 1 0 0 1 1 1c0 1.25.2 2.45.57 3.57a1 1 0 0 1-.25 1z"/></svg>
        <span>+49 711 402 31958</span>
      </li>
      <li>
        <svg viewBox="0 0 24 24"><rect x="6" y="2" width="12" height="20" rx="2" fill="none" stroke="var(--brand)" stroke-width="2"/><circle cx="12" cy="18" r="1.2" fill="var(--brand)"/></svg>
        <span>+49 711 402 31900</span>
      </li>
      <li>
        <svg viewBox="0 0 24 24"><rect x="2" y="5" width="20" height="14" rx="1" fill="var(--brand)"/><path d="M2.5 6 L12 13 L21.5 6" fill="none" stroke="var(--paper)" stroke-width="1.5"/></svg>
        <span>info@vorelta.de</span>
      </li>
    </ul>

    <p class="website">www.vorelta.de</p>
  </section>

</body>
</html>
```